Ardenwell Building and Property Services needs a business card design

We need a business card design for our building and property services business. We already have a logo we just need a creative design and layout on a business card. Emphasis on clean, modern, professional.
Our client targets are mainly body corporates, building managers, construction managers.
We are a building services company that lean more to structural repair of buildings, through concrete rectification and carbon fibre strengthening.
We also refurbish facades, rendering, painting etc
We target higher end body corporates in prestigious locations, hence why we'd like our cards to reflect professionalism, strength, efficiency

Target Market(s)

body corporates, building managers, construction managers

Industry/Entity Type

Construction

Contact Information for Business Card

Ardenwell is the main word, with 'Building and Property Services' underneath.
Level 17, 82 Harlow Street
MERRIDALE
Melbourne
Vic 3094
T: 9518 2736
Duncan Ferris - Director
dunardenwell@mailbox-example.com

Requirements
Must have
• Stand out on the back of the card- strong/ bold, company logo
• All of the contact details written above
Should not have
• I'd like the card to stand out, especially on the back. Id like the company logo to be prominent, although feel free to be creative around it. But remain clean and professional

```html
<!DOCTYPE html>
<html lang="en">
<head>
<meta charset="utf-8">
<title>Ardenwell Building and Property Services – Business Card</title>
<link href="https://fonts.googleapis.com/css2?family=Lato:wght@400;700&display=swap" rel="stylesheet">
<style>
  :root {
    --stage: #2a2a2c;
    --card: #111114;
    --card-edge: #1a1a1e;
    --brand-blue: #2a8fdc;
    --pattern-navy: #0d1a3a;
    --pattern-deep: #0a0d1c;
    --text-light: #e6e8ec;
    --text-muted: #b9bcc3;
    --divider: #8a8d94;
  }
  * { box-sizing: border-box; margin: 0; padding: 0; }
  html, body {
    width: 1200px; height: 900px; overflow: hidden;
    background: var(--stage);
    font-family: "Lato", Arial, sans-serif;
  }
  .canvas {
    position: relative; width: 1200px; height: 900px;
  }
  .card {
    position: absolute; width: 700px; height: 400px;
    background: var(--card);
    border: 1px solid var(--card-edge);
    box-shadow: 0 10px 30px rgba(0,0,0,0.45);
    overflow: hidden;
  }
  /* Back of card */
  .card-back { left: 250px; top: 40px; }
  .card-back .pattern-field {
    position: absolute; inset: 0;
    background: radial-gradient(ellipse at center, var(--pattern-navy) 0%, var(--pattern-deep) 75%);
  }
  .card-back .brand {
    position: absolute; inset: 0;
    display: flex; flex-direction: column; align-items: center; justify-content: center;
    gap: 10px;
  }
  .brand-name {
    font-weight: 700; color: var(--brand-blue);
    letter-spacing: 6px; text-transform: uppercase;
  }
  .card-back .brand-name { font-size: 54px; }
  .brand-tagline {
    color: var(--text-muted); text-transform: uppercase;
    letter-spacing: 2.5px; font-size: 13px;
  }
  /* Front of card */
  .card-front { left: 250px; top: 470px; }
  .card-front .brand {
    position: absolute; left: 0; top: 0; width: 390px; height: 400px;
    display: flex; flex-direction: column; align-items: center; justify-content: center; gap: 8px;
  }
  .card-front .brand-name { font-size: 44px; letter-spacing: 5px; }
  .card-front .brand-tagline { font-size: 11px; letter-spacing: 2px; }
  .divider {
    position: absolute; left: 392px; top: 50px; width: 1.5px; height: 300px;
    background: var(--divider);
  }
  .contact {
    position: absolute; left: 430px; top: 52px; right: 20px;
    font-size: 14.5px; color: var(--text-muted);
  }
  .contact-name { color: var(--brand-blue); font-weight: 700; font-size: 17px; }
  .contact-role { color: var(--text-light); font-weight: 700; font-size: 16px; margin-bottom: 12px; }
  .contact-line { display: flex; align-items: center; gap: 8px; margin-bottom: 4px; }
  .contact-line svg { flex: none; }
  .address { margin-top: 70px; margin-left: 40px; line-height: 1.35; font-size: 16px; }
</style>
</head>
<body>
<div class="canvas">

  <section class="card card-back">
    <div class="pattern-field" role="img" aria-label="Faint navy line pattern repeating the brand mark across the card back"></div>
    <div class="brand">
      <div class="brand-name">Ardenwell</div>
      <div class="brand-tagline">Building and Property Services</div>
    </div>
  </section>

  <section class="card card-front">
    <div class="brand">
      <div class="brand-name">Ardenwell</div>
      <div class="brand-tagline">Building and Property Services</div>
    </div>
    <div class="divider"></div>
    <div class="contact">
      <div class="contact-name">Duncan Ferris</div>
      <div class="contact-role">Director</div>
      <div class="contact-line">
        <svg width="16" height="12" viewBox="0 0 16 12" aria-hidden="true">
          <path d="M1 4 Q8 -1 15 4 L13 6 L11 4.5 L5 4.5 L3 6 Z" fill="var(--brand-blue)"/>
          <rect x="3" y="6.5" width="10" height="5" rx="1" fill="var(--brand-blue)"/>
        </svg>
        <span>9518 2736</span>
      </div>
      <div class="contact-line">
        <svg width="16" height="12" viewBox="0 0 16 12" aria-hidden="true">
          <rect x="1" y="1" width="14" height="10" fill="var(--brand-blue)"/>
          <path d="M1 1 L8 7 L15 1" stroke="var(--card)" stroke-width="1.2" fill="none"/>
        </svg>
        <span>dunardenwell@mailbox-example.com</span>
      </div>
      <div class="address">
        Level 17, 82 Harlow Street<br>
        MERRIDALE<br>
        Melbourne<br>
        Vic 3094
      </div>
    </div>
  </section>

</div>
</body>
</html>
```